Redesign for luxury lifestyle PR agency

Ginger Kite Otter is a luxury lifestyle public relations agency specialising in indigenous and regenerative travel. We are the elephant you want in the room. We represent interesting brands and people who would be described as changemakers in their respective fields. The winning design should be stylish, clean cut and earthy. It should communicate that Ginger Kite Otter is professional and representative of the industries that it serves. The purpose of the website is to provide clear information to potential customers and media, improve the image and brand of the company, position the company as one of scale and increase sales conversions. Its aesthetic will be aspirational and image led in an editorial style. I would like to be able to easily edit the website once finished and be able to work with the designer on an ad hoc basis once the project is completed.

Please see below for some website I like the style of:

https://www.velmora-ensemble.com/

https://www.tasbergglobal.com/

https://www.brindlequarterly.co.uk/

Pages I would like to include are:

Home
Services
Clients
Testimonials
About Us
News

I'm also attaching a proposal that I really liked the style of and I would like this sort of aesthetic on the website too. My logo is also attached (it is likely that the colour palette might change with the website).

I'm open to inspiration on the colours - my immediate preference is greens and/or blues.

Here is the existing website that I built myself on Wix - https://www.gingerkiteotter.com/ (it looks so outdated and amateur now hence the need of a serious rebrand)

Target Market(s)

Luxury travel and lifestyle brands

Industry/Entity Type

Luxury travel and lifestyle

Number of Pages Required

1 page

Font styles to use
Serif
Other font styles liked:
• Open to suggestions

Requirements
Must have
• Beautiful imagery

```html
<!DOCTYPE html>
<html lang="en">
<head>
<meta charset="utf-8">
<title>Ginger Kite Otter — Lifestyle PR</title>
<link rel="stylesheet" href="https://fonts.googleapis.com/css2?family=Jost:wght@400;500;600;700&display=swap">
<style>
:root{
  --blue:#0b5fb5;
  --blue-deep:#0a4ea6;
  --ink:#111111;
  --text:#333333;
  --pale:#d8e8f5;
  --footer:#1b2030;
  --white:#ffffff;
}
*{box-sizing:border-box;margin:0;padding:0}
html,body{width:1200px;height:4724px;overflow:hidden;background:var(--white)}
body{font-family:'Jost',sans-serif;color:var(--ink);position:relative}
.abs{position:absolute}
section,header,footer{position:absolute;left:0;width:1200px}
.ph{position:absolute;overflow:hidden}
/* header */
.site-header{top:0;height:118px;background:var(--white)}
.brand{left:143px;top:34px;width:200px}
.brand-mark{display:block;width:16px;height:16px;border-radius:50%;background:var(--blue);margin:0 0 6px 28px}
.brand-name{font-size:23px;font-weight:500;color:var(--blue);line-height:1.02;letter-spacing:.5px}
.top-phone{left:625px;top:17px;font-size:22px;font-weight:500;display:flex;align-items:center;gap:8px}
.top-phone .ring{width:30px;height:30px;border-radius:50%;background:var(--blue);display:flex;align-items:center;justify-content:center}
.main-nav{left:364px;top:75px;display:flex;gap:34px;font-size:15px;font-weight:500;text-transform:uppercase}
.main-nav span:first-child::before{content:"";display:inline-block;width:10px;height:10px;border-radius:50%;background:var(--blue);margin-right:8px}
.btn{display:flex;align-items:center;justify-content:center;border-radius:26px;font-weight:600;text-transform:uppercase;color:var(--white);background:var(--blue)}
.login{left:930px;top:60px;width:124px;height:48px;font-size:17px}
/* hero */
.hero{top:118px;height:551px}
.hero-img{position:absolute;inset:0;background:
  radial-gradient(ellipse 120px 330px at 470px 330px,rgba(35,60,95,.75),rgba(35,60,95,0)),
  radial-gradient(ellipse 90px 200px at 860px 420px,rgba(40,60,90,.7),rgba(40,60,90,0)),
  radial-gradient(ellipse 700px 160px at 600px 520px,rgba(70,95,125,.9),rgba(70,95,125,0)),
  linear-gradient(180deg,#0b3e96 0%,#1d5cb2 30%,#4f7fb8 55%,#6f8aa6 75%,#3f5877 100%)}
.hero h1{left:146px;top:136px;font-size:42px;font-weight:600;line-height:51px;color:var(--white);letter-spacing:1px;text-shadow:0 2px 6px rgba(0,0,0,.35)}
.hero p{left:146px;top:262px;width:480px;font-size:14px;line-height:24px;color:var(--white);text-shadow:0 1px 3px rgba(0,0,0,.4)}
.hero .cta{left:146px;top:358px;width:179px;height:48px;border:2px solid var(--white);font-size:16px}
.hero-dot{width:9px;height:9px;border-radius:50%;background:var(--white);left:1113px}
/* shared headings */
.sec-mark{width:18px;height:18px;border-radius:50%;background:var(--blue);left:591px}
.sec-title{left:0;width:1200px;text-align:center;font-size:42px;font-weight:600;letter-spacing:1.5px;text-transform:uppercase}
.sec-sub{left:0;width:1200px;text-align:center;font-size:17px;line-height:25px;color:var(--text)}
.arrow{width:44px;height:44px;border-radius:50%;border:1.5px solid #666;background:var(--white);display:flex;align-items:center;justify-content:center}
.plus{width:28px;height:28px;border-radius:50%;background:var(--white);display:flex;align-items:center;justify-content:center}
/* services */
.services{top:669px;height:649px}
.svc{position:absolute;width:217px;top:271px}
.svc .ph{position:relative;height:221px}
.svc.active .ph{outline:4px solid var(--blue);outline-offset:-4px}
.svc h3{margin-top:14px;text-align:center;font-size:21px;font-weight:600;line-height:26px}
/* clients */
.clients{top:1318px;height:645px;background:linear-gradient(180deg,#0b55b0,#1574c4)}
.clients .sec-title,.clients .sec-sub{color:var(--white)}
.cl{top:277px;height:273px}
.cl.active{outline:3px solid var(--white)}
/* past */
.past{top:1963px;height:1227px}
.tile{width:290px;height:273px}
.load{left:510px;top:1117px;width:180px;height:50px;font-size:17px}
/* who */
.who{top:3190px;height:645px;background:var(--pale)}
.who h2{left:148px;top:145px;font-size:44px;font-weight:600;letter-spacing:2px}
.who p{left:148px;top:218px;width:502px;font-size:13px;line-height:25.5px;color:var(--text);text-align:justify}
.who .more{left:148px;top:487px;width:180px;height:48px;font-size:17px}
.portrait{left:745px;top:75px;width:362px;height:495px}
.dots{background:rgba(11,95,181,.18);border-radius:8px}
/* contact */
.contact{top:3835px;height:743px}
.contact-line{left:0;width:1200px;top:252px;display:flex;justify-content:center;align-items:center;gap:14px;font-size:18px;font-weight:500}
.field{border:1px solid #aaa;background:var(--white);font-size:15px;color:#444;padding:16px 20px}
.submit{left:510px;top:611px;width:180px;height:48px;font-size:17px}
/* footer */
.site-footer{top:4578px;height:146px;background:var(--footer);color:var(--white)}
.news h4{position:absolute;left:145px;top:40px;font-size:16px;font-weight:600}
.news .in{position:absolute;left:145px;top:73px;width:185px;height:36px;background:var(--white);color:#444;font-size:12px;padding:10px 15px}
.news .go{position:absolute;left:330px;top:73px;width:105px;height:36px;background:var(--blue);font-size:13px;font-weight:600;display:flex;align-items:center;justify-content:center}
.foot-nav{left:558px;top:60px;display:flex;gap:37px;font-size:15px;font-weight:500}
.legal{left:558px;top:98px;font-size:12px;opacity:.9}
</style>
</head>
<body>

<header class="site-header">
  <div class="abs brand">
    <span class="brand-mark"></span>
    <div class="brand-name">GINGER KITE<br>OTTER</div>
  </div>
  <div class="abs top-phone">
    <span class="ring"><svg width="16" height="16" viewBox="0 0 24 24"><path fill="#fff" d="M6.6 10.8a15 15 0 006.6 6.6l2.2-2.2c.3-.3.7-.4 1-.2 1.1.4 2.3.6 3.6.6.6 0 1 .4 1 1V20c0 .6-.4 1-1 1A17 17 0 013 4c0-.6.4-1 1-1h3.5c.6 0 1 .4 1 1 0 1.3.2 2.5.6 3.6.1.3 0 .7-.2 1z"/></svg></span>
    +44 (0) 7700 900418
  </div>
  <nav class="abs main-nav"><span>Home</span><span>Services</span><span>Clients</span><span>Who we are</span><span>Contact</span></nav>
  <div class="abs btn login">Login</div>
</header>

<section class="hero">
  <div class="hero-img" role="img" aria-label="City skyline with tall glass towers under a deep blue sky"></div>
  <h1 class="abs">THE ELEPHANT YOU<br>WANT IN THE ROOM</h1>
  <p class="abs">Ginger Kite Otter is a boutique lifestyle PR and communications agency helping brands get their voices heard in the UK.</p>
  <div class="abs btn cta">Get Started</div>
  <span class="abs hero-dot" style="top:242px"></span>
  <span class="abs hero-dot" style="top:297px"></span>
</section>

<section class="services">
  <span class="abs sec-mark" style="top:66px"></span>
  <h2 class="abs sec-title" style="top:92px">Services</h2>
  <p class="abs sec-sub" style="top:167px">No-nonsense approach to launching new brands to the UK market, offering<br>a completely bespoke service to include</p>
  <div class="abs arrow" style="left:63px;top:360px"><svg width="14" height="14" viewBox="0 0 14 14"><path d="M9 2L4 7l5 5" stroke="#333" stroke-width="2" fill="none"/></svg></div>
  <div class="abs arrow" style="left:1091px;top:360px"><svg width="14" height="14" viewBox="0 0 14 14"><path d="M5 2l5 5-5 5" stroke="#333" stroke-width="2" fill="none"/></svg></div>
  <div class="svc" style="left:145px"><div class="ph" role="img" aria-label="Team reviewing printed charts on a desk" style="background:radial-gradient(circle at 40% 70%,#e9e6e0 0,rgba(233,230,224,0) 55%),radial-gradient(circle at 80% 20%,#3d4350 0,rgba(61,67,80,0) 50%),linear-gradient(135deg,#5b6270,#b9b4ac 60%,#d8d2c8)"></div><h3>Strategic<br>Planning</h3></div>
  <div class="svc active" style="left:375px"><div class="ph" role="img" aria-label="Colleagues working together on laptops" style="background:radial-gradient(circle at 30% 55%,#5a3f30 0,rgba(90,63,48,0) 40%),radial-gradient(circle at 75% 60%,#a58b70 0,rgba(165,139,112,0) 45%),linear-gradient(180deg,#7b8088 0%,#4c4f55 45%,#2c2e33 100%)"></div><h3>Consumer Media<br>Relations</h3></div>
  <div class="svc" style="left:607px"><div class="ph" role="img" aria-label="Monitor showing a reputation graph" style="background:radial-gradient(ellipse 90px 70px at 55% 45%,#f2f2f2 0,#f2f2f2 60%,rgba(242,242,242,0) 100%),radial-gradient(ellipse 120px 100px at 50% 45%,#2d3036 0,rgba(45,48,54,0) 100%),linear-gradient(180deg,#e9e9e9,#b8bcc2)"></div><h3>Reputation<br>Management</h3></div>
  <div class="svc" style="left:838px"><div class="ph" role="img" aria-label="Woman looking at her phone with social reactions" style="background:radial-gradient(ellipse 60px 90px at 45% 70%,#f5f5f3 0,rgba(245,245,243,0) 100%),radial-gradient(ellipse 55px 70px at 45% 28%,#3a2a22 0,rgba(58,42,34,0) 100%),linear-gradient(135deg,#d9d7d3,#a89e96)"></div><h3>Influencer<br>Engagement</h3></div>
</section>

<section class="clients">
  <span class="abs sec-mark" style="top:73px;background:var(--white)"></span>
  <h2 class="abs sec-title" style="top:100px">Clients</h2>
  <p class="abs sec-sub" style="top:184px">A dynamic collection of innovative lifestyle clients that we are wholly passionate about</p>
  <div class="abs arrow" style="left:63px;top:392px"><svg width="14" height="14" viewBox="0 0 14 14"><path d="M9 2L4 7l5 5" stroke="#333" stroke-width="2" fill="none"/></svg></div>
  <div class="abs arrow" style="left:1091px;top:392px"><svg width="14" height="14" viewBox="0 0 14 14"><path d="M5 2l5 5-5 5" stroke="#333" stroke-width="2" fill="none"/></svg></div>
  <div class="ph cl" style="left:145px;width:289px;background:radial-gradient(ellipse 90px 80px at 45% 85%,#3a2a20 0,rgba(58,42,32,0) 100%),radial-gradient(ellipse 130px 90px at 55% 35%,#c9957a 0,rgba(201,149,122,0) 100%),linear-gradient(180deg,#eef0f2,#d7c6b8)" role="img" aria-label="Raised crossed arms wearing rings against a pale sky"></div>
  <div class="ph cl active" style="left:453px;width:294px;background:radial-gradient(ellipse 110px 40px at 50% 12%,#3ab6ae 0,#2a9b94 60%,rgba(42,155,148,0) 100%),radial-gradient(ellipse 100px 90px at 50% 55%,#1f1d1c 0,rgba(31,29,28,0) 100%),linear-gradient(90deg,#8a3f28,#b0603f 20%,#5a2f22 50%,#b0603f 80%,#8a3f28)" role="img" aria-label="Restaurant storefront with a teal awning"><div class="abs plus" style="left:133px;top:122px"><svg width="12" height="12" viewBox="0 0 12 12"><path d="M6 1v10M1 6h10" stroke="#0b5fb5" stroke-width="2"/></svg></div></div>
  <div class="ph cl" style="left:766px;width:289px;background:radial-gradient(ellipse 70px 90px at 50% 50%,#3b3f4a 0,rgba(59,63,74,0) 100%),radial-gradient(ellipse 95px 120px at 50% 50%,#a68545 0,#8c6c33 70%,rgba(140,108,51,0) 100%),linear-gradient(135deg,#f2f2f0,#dedcd8)" role="img" aria-label="Framed portrait painting on a white wall"></div>
</section>

<section class="past">
  <span class="abs sec-mark" style="top:78px"></span>
  <h2 class="abs sec-title" style="top:105px">Past Clients</h2>
  <div class="ph tile" style="left:145px;top:208px;background:radial-gradient(ellipse 110px 240px at 15% 70%,#4a2e3a 0,rgba(74,46,58,0) 100%),linear-gradient(180deg,#b94fb0 0%,#e26fa1 50%,#f2a07f 100%)" role="img" aria-label="Hotel facade with a neon sign at dusk"></div>
  <div class="ph tile" style="left:455px;top:208px;background:radial-gradient(ellipse 120px 80px at 50% 70%,#6f9bcc 0,rgba(111,155,204,0) 100%),linear-gradient(180deg,#3f7cc4,#2e63a5)" role="img" aria-label="Hotel lobby under a blue overlay"><div class="abs plus" style="left:131px;top:122px"><svg width="12" height="12" viewBox="0 0 12 12"><path d="M6 1v10M1 6h10" stroke="#0b5fb5" stroke-width="2"/></svg></div></div>
  <div class="ph tile" style="left:765px;top:208px;background:radial-gradient(ellipse 50px 60px at 55% 50%,#5f6e6a 0,rgba(95,110,106,0) 100%),linear-gradient(180deg,#6c8c4e 0%,#8ea36a 40%,#e7e0d4 62%,#d8cfc2 100%)" role="img" aria-label="Garden pool with a sculpture"></div>
  <div class="ph tile" style="left:145px;top:503px;background:radial-gradient(ellipse 70px 30px at 62% 55%,#f4f4f4 0,rgba(244,244,244,0) 100%),linear-gradient(180deg,#5ea3dc 0%,#9fc9ea 45%,#d9c8a4 60%,#cdb585 100%)" role="img" aria-label="SUV parked on a beach beside surfboards"></div>
  <div class="ph tile" style="left:455px;top:503px;background:radial-gradient(ellipse 110px 45px at 45% 58%,#b8a78a 0,rgba(184,167,138,0) 100%),linear-gradient(180deg,#8fb8e0 0%,#a9b8bf 25%,#3a76b5 45%,#1a4f8c 100%)" role="img" aria-label="Aerial view of a coastal island town"></div>
  <div class="ph tile" style="left:765px;top:503px;background:radial-gradient(ellipse 150px 60px at 50% 80%,#1f8486 0,rgba(31,132,134,0) 100%),linear-gradient(180deg,#9fd3d0 0%,#63bdb8 40%,#3aa19d 100%)" role="img" aria-label="Hammock over turquoise sea water"></div>
  <div class="ph tile" style="left:145px;top:798px;background:radial-gradient(ellipse 90px 60px at 45% 60%,#e9e2a8 0,rgba(233,226,168,0) 100%),radial-gradient(ellipse 120px 120px at 45% 55%,#4f5a2c 0,rgba(79,90,44,0) 100%),linear-gradient(135deg,#e4788a,#c8702f)" role="img" aria-label="Layered dessert with a pistachio crust"></div>
  <div class="ph tile" style="left:455px;top:798px;background:radial-gradient(ellipse 60px 40px at 50% 40%,#6b4630 0,rgba(107,70,48,0) 100%),radial-gradient(ellipse 90px 60px at 50% 38%,#f2f0ec 0,rgba(242,240,236,0) 100%),linear-gradient(180deg,#2b2b2b,#7b7b7b 60%,#dcdcdc)" role="img" aria-label="Pour-over coffee brewing"></div>
  <div class="ph tile" style="left:765px;top:798px;background:radial-gradient(ellipse 60px 70px at 50% 58%,#f6f6f4 0,rgba(246,246,244,0) 100%),radial-gradient(ellipse 120px 110px at 50% 62%,#2f4f8e 0,rgba(47,79,142,0) 100%),linear-gradient(180deg,#6f7a66,#3c4560)" role="img" aria-label="Table setting with a blue patterned plate and napkin"></div>
  <div class="abs btn load">Load More</div>
</section>

<section class="who">
  <span class="abs sec-mark" style="left:148px;top:116px"></span>
  <h2 class="abs">WHO WE ARE</h2>
  <p class="abs">Maren Holloway founded Ginger Kite Otter in 2016 after working for one of the most reputable luxury travel PR agencies in London, leading a team that launched some of the world's most iconic hotels, as well as spending time at a national newspaper. She understands what it is like to be on either side of the PR coin and what it takes to create a juicy story.<br>Ginger Kite Otter works as an extension to your team providing a service that feels in-house. Maren prefers a direct approach and will always pick up the phone to sound out an idea and probably ask what you're planning for dinner too. The Ginger Kite Otter clients are a carefully curated list and they feel like family.</p>
  <div class="abs btn more">Read More</div>
  <div class="abs dots" style="left:1110px;top:250px;width:65px;height:385px" role="img" aria-label="Blue dot pattern"></div>
  <div class="abs dots" style="left:830px;top:580px;width:345px;height:55px" role="img" aria-label="Blue dot pattern"></div>
  <div class="ph portrait" style="background:radial-gradient(ellipse 110px 150px at 48% 40%,#9c9c9c 0,rgba(156,156,156,0) 100%),radial-gradient(ellipse 170px 260px at 45% 45%,#1e1e1e 0,rgba(30,30,30,0) 100%),linear-gradient(180deg,#8a8a8a,#d8d8d8 70%,#bdbdbd)" role="img" aria-label="Black and white portrait of the agency founder"></div>
</section>

<section class="contact">
  <span class="abs sec-mark" style="top:86px"></span>
  <h2 class="abs sec-title" style="top:113px">Contact</h2>
  <p class="abs sec-sub" style="top:198px">The best relationships start at hello....</p>
  <div class="abs contact-line">
    <svg width="18" height="14" viewBox="0 0 18 14"><rect width="18" height="14" rx="1" fill="#0b5fb5"/><path d="M1 1l8 6 8-6" stroke="#fff" stroke-width="1.5" fill="none"/></svg>
    <span>maren@gingerkiteotter.com</span><span>|</span>
    <svg width="18" height="18" viewBox="0 0 24 24"><path fill="#0b5fb5" d="M6.6 10.8a15 15 0 006.6 6.6l2.2-2.2c.3-.3.7-.4 1-.2 1.1.4 2.3.6 3.6.6.6 0 1 .4 1 1V20c0 .6-.4 1-1 1A17 17 0 013 4c0-.6.4-1 1-1h3.5c.6 0 1 .4 1 1 0 1.3.2 2.5.6 3.6.1.3 0 .7-.2 1z"/></svg>
    <span>+44 (0) 7700 900418</span>
  </div>
  <div class="abs field" style="left:233px;top:325px;width:360px;height:52px">First Name</div>
  <div class="abs field" style="left:605px;top:325px;width:360px;height:52px">Last Name</div>
  <div class="abs field" style="left:233px;top:390px;width:360px;height:52px">Email address</div>
  <div class="abs field" style="left:605px;top:390px;width:360px;height:52px">Phone Number</div>
  <div class="abs field" style="left:233px;top:454px;width:732px;height:115px">Message</div>
  <div class="abs btn submit">Submit</div>
</section>

<footer class="site-footer">
  <div class="news">
    <h4>SIGN UP NEWSLETTER</h4>
    <div class="in">Enter Email</div>
    <div class="go">SIGN UP</div>
  </div>
  <nav class="abs foot-nav"><span>HOME</span><span>SERVICES</span><span>CLIENTS</span><span>WHO WE ARE</span><span>CONTACT</span></nav>
  <div class="abs legal">© 2022 Ginger Kite Otter . All rights reserved &nbsp;|&nbsp; Privacy &nbsp;|&nbsp; Terms of Use</div>
</footer>

</body>
</html>
```